Bref créative
Business Card, Stationary, and #10 Envelope
Bright Harbor Advising
I need double sided standard sized Business Card [3.5" x 2"]
Logo font was Brussels, please use the same, similar or compatible font
Professional
Milo Trenholt
Certified College Planning Specialist
4870 Quarlow Lane
Fargo, North Dakota 58246
milo@brightharboradvising.example
www.brightharboradvising.example
Would like the colors of the card to match the logo. Gold/yellow, black, and white. 2 designs are included, one with a gold tag line, and one with a black tag line. I prefer the gold tag line so I am hoping your designs can utilize that coloring but I am open to ideas.
We can help you:
-Afford college while protecting retirement
-Lower the total cost of college
-Maximize financial aid qualification
-Compare the net cost of public vs private schools
Logo
Logo 2

```html
<!DOCTYPE html>
<html lang="en">
<head>
<meta charset="utf-8">
<title>Bright Harbor Advising — We can help you</title>
<link href="https://fonts.googleapis.com/css2?family=Arimo:wght@400;700&display=swap" rel="stylesheet">
<style>
  :root {
    --paper: #ffffff;
    --ink: #111111;
    --text: #1c1c1c;
    --gold: #c9a227;
    --edge: #b9b9b9;
    --silhouette: #0d0d0d;
  }
  html, body {
    margin: 0;
    padding: 0;
    width: 1200px;
    height: 686px;
    overflow: hidden;
    background: var(--paper);
  }
  .card {
    position: relative;
    width: 1200px;
    height: 686px;
    box-sizing: border-box;
    border: 3px solid var(--edge);
    background: var(--paper);
    font-family: "Arimo", Arial, sans-serif;
    color: var(--text);
  }
  .brand {
    position: absolute;
    left: 90px;
    top: 78px;
    display: flex;
    align-items: center;
    gap: 16px;
  }
  .brand-dot {
    width: 46px;
    height: 46px;
    border-radius: 50%;
    background: var(--gold);
    flex: none;
  }
  .brand-name {
    font-weight: 700;
    font-size: 28px;
    color: var(--ink);
    letter-spacing: 0.3px;
  }
  .services-title {
    position: absolute;
    left: 91px;
    top: 328px;
    margin: 0;
    font-size: 37px;
    font-weight: 700;
    color: var(--ink);
  }
  .services {
    position: absolute;
    left: 44px;
    top: 418px;
    margin: 0;
    padding: 0;
    list-style: none;
  }
  .services li {
    display: flex;
    align-items: center;
    height: 63px;
    font-size: 31px;
    color: var(--text);
  }
  .services li:last-child { font-size: 32px; }
  .tick {
    width: 22px;
    height: 22px;
    margin-right: 22px;
    flex: none;
  }
  .graduates {
    position: absolute;
    left: 782px;
    top: 142px;
    width: 388px;
    height: 448px;
    border-radius: 60px 60px 8px 8px;
    background: linear-gradient(180deg, #2a2a2a 0%, var(--silhouette) 100%);
  }
</style>
</head>
<body>
  <main class="card">
    <div class="brand">
      <span class="brand-dot"></span>
      <span class="brand-name">Bright Harbor Advising</span>
    </div>

    <h2 class="services-title">We can help you</h2>
    <ul class="services">
      <li><svg class="tick" viewBox="0 0 22 22" aria-hidden="true"><path d="M3 12 L9 18 L19 4" fill="none" stroke="#1c1c1c" stroke-width="2"/></svg>Afford college while protecting retirement</li>
      <li><svg class="tick" viewBox="0 0 22 22" aria-hidden="true"><path d="M3 12 L9 18 L19 4" fill="none" stroke="#1c1c1c" stroke-width="2"/></svg>Lower the total cost of college</li>
      <li><svg class="tick" viewBox="0 0 22 22" aria-hidden="true"><path d="M3 12 L9 18 L19 4" fill="none" stroke="#1c1c1c" stroke-width="2"/></svg>Maximize financial aid qualification</li>
      <li><svg class="tick" viewBox="0 0 22 22" aria-hidden="true"><path d="M3 12 L9 18 L19 4" fill="none" stroke="#1c1c1c" stroke-width="2"/></svg>Compare the net cost of public vs private</li>
    </ul>

    <div class="graduates" role="img" aria-label="Black silhouettes of four graduates in caps and gowns standing together"></div>
  </main>
</body>
</html>
```